Creative Stationary For Security Solutions Company
Halvern Guard Services
Creative Stationary For Security Solutions Company - Security
Creative Brief
Professional
Wesley Kolvasky
wesley@halvernguard.example
www.halvernguard.example
California PI No. 51928 And California PPO No. 40261
Logo has been uploaded in different color variations. Feel free to experiment, however I prefer the logo with black highlights on the visor, nose and neck (#1 I believe) I will provide my phone numbers towards the end of the project. Thanks and have fun.
I would like to see my logo on one side and info on the other. But feel free to experiment.

```html
<!DOCTYPE html>
<html lang="en">
<head>
<meta charset="utf-8">
<title>Halvern Guard Services – Business Card</title>
<link rel="stylesheet" href="https://fonts.googleapis.com/css2?family=Montserrat:wght@400;600;800&display=swap">
<style>
  :root {
    --stage: #e6e6e6;
    --card-white: #f7f7f7;
    --card-black: #1c1c1c;
    --card-black-soft: #262626;
    --ink: #222222;
    --ink-muted: #555555;
    --orange: #f26a1b;
    --white: #ffffff;
  }
  * { margin: 0; padding: 0; box-sizing: border-box; }
  html, body {
    width: 1200px; height: 980px; overflow: hidden;
    background: var(--stage);
    font-family: "Montserrat", Arial, sans-serif;
  }
  .stage {
    position: relative; width: 1200px; height: 980px;
  }
  .card {
    position: absolute; left: 200px; width: 800px; height: 457px;
    border-radius: 26px; overflow: hidden;
    box-shadow: 0 8px 24px rgba(0,0,0,.18);
  }
  .card--front { top: 22px; background: var(--card-white); }
  .card--back { top: 501px; background: var(--card-black); }
  .card-art { position: absolute; inset: 0; width: 100%; height: 100%; }

  .contact-list {
    position: absolute; left: 58px; top: 78px; list-style: none;
  }
  .contact-item {
    display: flex; align-items: center; gap: 10px;
    height: 25px; font-size: 14px; color: var(--ink-muted);
  }
  .contact-icon { width: 16px; height: 16px; flex: none; }

  .brand {
    position: absolute; left: 340px; top: 170px;
    display: flex; align-items: center; gap: 14px;
  }
  .brand-dot {
    width: 54px; height: 54px; border-radius: 50%; background: var(--orange);
  }
  .brand-name {
    font-weight: 800; font-size: 30px; line-height: 1.05;
    color: var(--ink); letter-spacing: .5px; text-transform: uppercase;
  }

  .signatory {
    position: absolute; right: 50px; bottom: 30px; text-align: right; color: var(--white);
  }
  .signatory-name { font-size: 16px; font-weight: 600; }
  .signatory-role { font-size: 12px; font-weight: 400; opacity: .85; margin-top: 3px; }

  .back-url {
    position: absolute; left: 54px; top: 34px;
    font-size: 15px; font-weight: 600; letter-spacing: 3px; color: var(--orange);
  }
  .back-mark {
    position: absolute; right: 70px; top: 90px;
    width: 280px; height: 280px; border-radius: 50%; background: var(--card-black-soft);
  }
</style>
</head>
<body>
<main class="stage">

  <section class="card card--front" aria-label="Business card front">
    <svg class="card-art" viewBox="0 0 800 457" preserveAspectRatio="none" aria-hidden="true">
      <path d="M0 282 C 260 290, 540 305, 800 330 L800 457 L0 457 Z" fill="var(--orange)"/>
      <path d="M0 296 C 260 305, 540 320, 800 346 L800 457 L0 457 Z" fill="var(--card-white)"/>
      <path d="M0 306 C 260 316, 540 332, 800 358 L800 457 L0 457 Z" fill="var(--card-black)"/>
    </svg>

    <ul class="contact-list">
      <li class="contact-item">
        <svg class="contact-icon" viewBox="0 0 16 16"><circle cx="8" cy="8" r="8" fill="var(--orange)"/><path d="M5 4.5l1.6-.4.9 2-1 .8a5 5 0 0 0 2.6 2.6l.8-1 2 .9-.4 1.6c-3.6.2-6.7-2.9-6.5-6.5z" fill="#fff"/></svg>
        123 456 7890
      </li>
      <li class="contact-item">
        <svg class="contact-icon" viewBox="0 0 16 16"><circle cx="8" cy="8" r="8" fill="var(--orange)"/><rect x="5.5" y="3.5" width="5" height="9" rx="1" fill="#fff"/></svg>
        987 654 3210
      </li>
      <li class="contact-item">
        <svg class="contact-icon" viewBox="0 0 16 16"><circle cx="8" cy="8" r="8" fill="var(--orange)"/><rect x="4" y="6" width="8" height="5" fill="#fff"/><rect x="5.5" y="4" width="5" height="2" fill="#fff"/></svg>
        123 456 7890
      </li>
      <li class="contact-item">
        <svg class="contact-icon" viewBox="0 0 16 16"><circle cx="8" cy="8" r="8" fill="var(--orange)"/><rect x="4" y="5" width="8" height="6" fill="#fff"/><path d="M4 5l4 3.2L12 5" stroke="var(--orange)" fill="none"/></svg>
        wesley@halvernguard.example
      </li>
      <li class="contact-item">
        <svg class="contact-icon" viewBox="0 0 16 16"><circle cx="8" cy="8" r="8" fill="var(--orange)"/><circle cx="8" cy="8" r="4" fill="none" stroke="#fff" stroke-width="1.3"/><path d="M4 8h8M8 4v8" stroke="#fff" stroke-width="1"/></svg>
        www.halvernguard.example
      </li>
    </ul>

    <div class="brand">
      <span class="brand-dot"></span>
      <span class="brand-name">Halvern<br>Guard Services</span>
    </div>

    <div class="signatory">
      <p class="signatory-name">Wesley Kolvasky</p>
      <p class="signatory-role">Founder</p>
    </div>
  </section>

  <section class="card card--back" aria-label="Business card back">
    <p class="back-url">www.halvernguard.example</p>
    <span class="back-mark"></span>
  </section>

</main>
</body>
</html>
```